Business Card for a Mortgage Agent (myself)

I need a business card for my new job as Mortgage Agent. The Broker's logo is to be on the card as well as the brokerage License number. Not sure if to include a photo or not. Info to be on card.
Dante Roux
Mortgage Agent
Lic # M47105386
Cell: 905-614-2753
Email: danterouxk.ma@fennmail.com
Web: www.karlvostermortgages.com
TPW Brokerage Lic. # 73918

```html
<!DOCTYPE html>
<html lang="en">
<head>
<meta charset="utf-8">
<title>Dante Roux – Mortgage Agent Business Card</title>
<link href="https://fonts.googleapis.com/css2?family=Jost:wght@400;500;600&display=swap" rel="stylesheet">
<style>
  :root {
    --navy: #211a5c;
    --navy-deep: #18134a;
    --violet: #4c40d0;
    --gold: #fcc706;
    --white: #ffffff;
    --ground: #b0b1ac;
  }
  * { box-sizing: border-box; margin: 0; padding: 0; }
  html, body { width: 1200px; height: 801px; overflow: hidden; }
  body {
    background: var(--ground);
    font-family: "Jost", Arial, sans-serif;
    position: relative;
  }
  .card {
    position: absolute;
    width: 560px;
    height: 320px;
    border-bottom: 4px solid var(--gold);
    border-right: 3px solid var(--gold);
    box-shadow: 0 14px 28px rgba(0,0,0,0.28);
    overflow: hidden;
  }
  /* Front */
  .card-front { left: 50px; top: 70px; background: var(--white); }
  .top-band {
    position: absolute; left: 0; top: 0; width: 100%; height: 58px;
    background: var(--navy);
    border-bottom: 3px solid var(--gold);
  }
  .brand {
    position: absolute; left: 200px; top: 72px;
    color: var(--navy);
    text-align: center;
    width: 200px;
  }
  .brand-mark {
    display: flex; align-items: center; justify-content: center; gap: 10px;
  }
  .brand-square { width: 22px; height: 22px; background: var(--gold); }
  .brand-initials {
    font-size: 40px; font-weight: 600; letter-spacing: 10px; line-height: 1;
  }
  .brand-name {
    font-size: 12px; font-weight: 600; letter-spacing: 1px; text-transform: uppercase;
    margin-top: 6px;
  }
  .brand-license { font-size: 7px; letter-spacing: 0.5px; margin-top: 2px; }
  .agent {
    position: absolute; left: 44px; top: 228px;
  }
  .agent-name {
    color: var(--gold); font-size: 30px; font-weight: 400; letter-spacing: 1px;
    text-transform: uppercase; line-height: 1;
  }
  .agent-title {
    color: var(--navy); font-size: 15px; font-weight: 400; letter-spacing: 0.5px;
    text-transform: uppercase; margin-top: 4px;
  }
  .divider {
    position: absolute; left: 268px; top: 188px; width: 1px; height: 86px;
    background: var(--gold);
  }
  .contact {
    position: absolute; left: 288px; top: 176px;
    list-style: none; color: var(--navy);
    font-size: 14px; line-height: 23px;
  }
  .contact li { display: flex; align-items: center; gap: 6px; }
  .contact svg { width: 11px; height: 11px; flex: none; }
  .contact .lic { font-size: 15px; }
  /* Back */
  .card-back { left: 600px; top: 400px; background: var(--navy); }
  .back-field {
    position: absolute; inset: 0;
    background: linear-gradient(215deg, var(--navy-deep) 0%, var(--navy) 45%, var(--violet) 100%);
  }
  .back-mark {
    position: absolute; right: 60px; top: 140px;
    color: var(--gold); font-size: 26px; font-weight: 600; letter-spacing: 3px;
  }
</style>
</head>
<body>
  <section class="card card-front" aria-label="Business card front">
    <div class="top-band"></div>
    <div class="brand">
      <div class="brand-mark">
        <span class="brand-square"></span>
        <span class="brand-initials">TPW</span>
      </div>
      <div class="brand-name">Tallpine West Mortgage</div>
      <div class="brand-license">LICENSE #73918</div>
    </div>
    <div class="agent">
      <div class="agent-name">Dante Roux</div>
      <div class="agent-title">Mortgage Agent</div>
    </div>
    <div class="divider"></div>
    <ul class="contact">
      <li class="lic">Lic # M47105386</li>
      <li>
        <svg viewBox="0 0 12 12"><path fill="#fcc706" d="M2.5 1h2l1 3-1.3 1a6 6 0 0 0 2.8 2.8l1-1.3 3 1v2c0 .8-.7 1.5-1.5 1.5A9.5 9.5 0 0 1 1 2.5C1 1.7 1.7 1 2.5 1z"/></svg>
        905-614-2753
      </li>
      <li>
        <svg viewBox="0 0 12 12"><rect x="1" y="2.5" width="10" height="7" fill="none" stroke="#fcc706" stroke-width="1.2"/><path d="M1 2.5l5 4 5-4" fill="none" stroke="#fcc706" stroke-width="1.2"/></svg>
        danterouxk.ma@fennmail.com
      </li>
      <li>
        <svg viewBox="0 0 12 12"><circle cx="6" cy="6" r="5" fill="none" stroke="#fcc706" stroke-width="1.1"/><ellipse cx="6" cy="6" rx="2.2" ry="5" fill="none" stroke="#fcc706" stroke-width="1"/><path d="M1 6h10" stroke="#fcc706" stroke-width="1"/></svg>
        www.karlvostermortgages.com
      </li>
    </ul>
  </section>

  <section class="card card-back" aria-label="Business card back">
    <div class="back-field" role="img" aria-label="Repeating brand-square pattern in navy and violet tones"></div>
    <div class="back-mark">TPW</div>
  </section>
</body>
</html>
```